A Modern & Sleek "Coming Soon" Page for an A.I Recruiting App

For the “Coming Soon” website, a simple background with no people in it. I've attached an A.I image of what the page should generally look like.

- A single mobile phone as the main focus where the user actually clicks on the, “notify me” button (after entering their email address).
- In the background where the pillars/columns are seen in the example, should be subtle pad locks that are in their opened position with a key inside the lock. I've attached images to try to illustrate this idea, but they are far away in style from what I'm looking for.

SLOGAN: Unlocking the power of meaningful connections
LOGO/TITLE: Should be the name as shown in image with only the name "KelpLoop" on it
COLORS: Purplish/blue hues. Should not be too feminine
NOTE: The user should only click once when signing up/entering their email.

Product: A recruiting platform that matches employers/employees with A.I. and prioritizing cultural fit/values system before skills. The industry we are tackling first is the caregiving industry (nannies, tutors, elderly). All users will be background screened and that info lives on the blockchain. All users will have the option to review and be reviewed/rated.

```html
<!DOCTYPE html>
<html lang="en">
<head>
<meta charset="utf-8">
<title>KelpLoop — Coming Soon</title>
<link rel="stylesheet" href="https://fonts.googleapis.com/css2?family=Montserrat:wght@200;300;500;600&display=swap">
<style>
  :root {
    --bg-blue: #37608d;
    --bg-indigo: #3a3a86;
    --bg-violet: #5a21bd;
    --white: #ffffff;
    --ink-navy: #1b1f4a;
    --frame-dark: #111216;
    --frame-silver: #c9cbd1;
    --screen-top: #3b6fa3;
    --screen-bottom: #6a22c6;
    --button-start: #3d6e9c;
    --button-end: #6a24c8;
    --deco-glow: rgba(150, 120, 230, 0.16);
  }

  * { margin: 0; padding: 0; box-sizing: border-box; }

  html, body {
    width: 1200px;
    height: 667px;
    overflow: hidden;
  }

  body {
    font-family: "Montserrat", sans-serif;
    color: var(--white);
  }

  .coming-soon {
    position: relative;
    width: 1200px;
    height: 667px;
    overflow: hidden;
    background: linear-gradient(100deg, var(--bg-blue) 0%, var(--bg-indigo) 45%, var(--bg-violet) 100%);
  }

  .lock-backdrop {
    position: absolute;
    left: 380px;
    top: 120px;
    width: 720px;
    height: 480px;
    background: radial-gradient(ellipse at 45% 50%, var(--deco-glow) 0%, rgba(150, 120, 230, 0.06) 45%, rgba(150, 120, 230, 0) 70%);
  }

  .brand-title {
    position: absolute;
    top: 52px;
    left: 0;
    width: 100%;
    text-align: center;
    font-weight: 200;
    font-size: 58px;
    letter-spacing: 9px;
    line-height: 1;
    text-transform: uppercase;
  }

  .slogan {
    position: absolute;
    left: 511px;
    top: 238px;
    font-weight: 500;
    font-size: 49px;
    line-height: 83px;
    letter-spacing: 1px;
    text-transform: uppercase;
    text-shadow: 2px 3px 6px rgba(0, 0, 0, 0.45);
  }

  .phone {
    position: absolute;
    left: 127px;
    top: 130px;
    width: 206px;
    height: 466px;
    transform: rotate(-6deg);
    border-radius: 34px;
    background: var(--frame-dark);
    border: 3px solid var(--frame-silver);
    padding: 9px;
    box-shadow: 6px 10px 22px rgba(0, 0, 0, 0.35);
  }

  .phone-screen {
    position: relative;
    width: 100%;
    height: 100%;
    border-radius: 26px;
    overflow: hidden;
    background: linear-gradient(160deg, var(--screen-top) 0%, #4a4aa5 50%, var(--screen-bottom) 100%);
    display: flex;
    flex-direction: column;
    align-items: center;
  }

  .phone-notch {
    position: absolute;
    top: 0;
    left: 50%;
    transform: translateX(-50%);
    width: 100px;
    height: 18px;
    background: var(--frame-dark);
    border-radius: 0 0 12px 12px;
  }

  .screen-content {
    margin-top: 70px;
    display: flex;
    flex-direction: column;
    align-items: center;
    transform: rotate(-8deg);
  }

  .screen-brand {
    font-weight: 300;
    font-size: 21px;
    letter-spacing: 3px;
    color: var(--ink-navy);
    text-transform: uppercase;
  }

  .screen-slogan {
    margin-top: 26px;
    font-weight: 500;
    font-size: 13px;
    line-height: 29px;
    letter-spacing: 0.6px;
    text-align: center;
    text-transform: uppercase;
  }

  .email-field {
    margin-top: 16px;
    width: 152px;
    height: 44px;
    border: 1px solid var(--white);
    display: flex;
    align-items: center;
    justify-content: center;
    font-size: 9.5px;
    font-weight: 500;
    letter-spacing: 0.4px;
    text-transform: uppercase;
  }

  .notify-button {
    margin-top: 18px;
    width: 96px;
    height: 38px;
    border-radius: 19px;
    background: linear-gradient(90deg, var(--button-start), var(--button-end));
    display: flex;
    align-items: center;
    justify-content: center;
    font-size: 11.5px;
    font-weight: 600;
    letter-spacing: 0.5px;
    text-transform: uppercase;
  }
</style>
</head>
<body>
  <main class="coming-soon">
    <div class="lock-backdrop" role="img" aria-label="Faint open padlock with key over a circuit-board pattern"></div>

    <h1 class="brand-title">KelpLoop</h1>

    <div class="phone">
      <div class="phone-screen">
        <div class="phone-notch"></div>
        <div class="screen-content">
          <div class="screen-brand">KelpLoop</div>
          <p class="screen-slogan">Unlocking the<br>power of<br>meaningful<br>connections</p>
          <div class="email-field">Enter email here</div>
          <div class="notify-button">Notify me</div>
        </div>
      </div>
    </div>

    <p class="slogan">Unlocking the power<br>of meaningful<br>connections</p>
  </main>
</body>
</html>
```